Corvane Electronics, Inc. Business card

Incorporate a globe.
We repair electronics, sell electronic parts, and we recycle electronics. We've been in business since 1982. A technology feel to the card is preferred. I want to be able to give this card to a client from different industries and make it relate-able. I don't have a logo that I've been partial to in the past. It is not necessary in this case.

Target Market(s)

Consumer, Industrial, Business, Medical

Industry/Entity Type

Business

Contact Information for Business Card

4518 Maple Crest Blvd. Dallas, TX 75207
214-555-0187 main 214-555-0143 fax
Paul Bredesen VP

Font styles to use
Serif

Requirements
Must have
• Technology feel
Nice to have
• Metallic look
Should not have
• no pastel colors

```html
<!DOCTYPE html>
<html lang="en">
<head>
<meta charset="utf-8">
<title>Corvane Electronics, Inc. Business Card</title>
<link href="https://fonts.googleapis.com/css2?family=Lato:ital,wght@0,400;0,700;0,900;1,400&display=swap" rel="stylesheet">
<style>
  :root {
    --page: #e7e8ea;
    --charcoal: #4a4a4d;
    --charcoal-light: #6a6a6e;
    --charcoal-dark: #3a3a3d;
    --amber: #f6b04a;
    --sky: #41a9df;
    --blue: #1f7cc9;
    --blue-deep: #0e55a8;
    --ink: #2b2b2e;
    --white: #ffffff;
  }
  * { box-sizing: border-box; margin: 0; padding: 0; }
  html, body { width: 1200px; height: 1200px; overflow: hidden; }
  body {
    background: var(--page);
    font-family: "Lato", sans-serif;
    display: flex;
    flex-direction: column;
    align-items: center;
    justify-content: center;
    gap: 70px;
  }
  .card {
    position: relative;
    width: 880px;
    height: 503px;
    overflow: hidden;
    box-shadow: 0 10px 28px rgba(0,0,0,0.22);
  }

  /* Back side */
  .card-back {
    background: radial-gradient(ellipse at 50% 45%, var(--charcoal-light) 0%, var(--charcoal) 55%, var(--charcoal-dark) 100%);
    display: flex;
    flex-direction: column;
    align-items: center;
    justify-content: center;
    gap: 34px;
  }
  .brand-name {
    color: var(--amber);
    font-weight: 900;
    text-transform: uppercase;
    text-align: center;
    line-height: 1.05;
  }
  .card-back .brand-name { font-size: 58px; letter-spacing: 2px; }
  .back-web {
    color: var(--white);
    font-weight: 700;
    font-size: 20px;
    letter-spacing: 5px;
  }

  /* Front side */
  .card-front { background: var(--white); }
  .brand-tab {
    position: absolute;
    left: 70px;
    top: 0;
    width: 400px;
    height: 225px;
    background: linear-gradient(160deg, var(--charcoal-light), var(--charcoal-dark));
    border-radius: 0 0 18px 18px;
    display: flex;
    align-items: center;
    justify-content: center;
    padding: 0 30px;
  }
  .brand-tab .brand-name { font-size: 36px; letter-spacing: 1px; }
  .person {
    position: absolute;
    left: 44px;
    top: 262px;
    font-size: 38px;
    font-weight: 900;
    color: var(--ink);
  }
  .person .first { color: var(--blue); }
  .rule {
    position: absolute;
    left: 44px;
    top: 314px;
    width: 680px;
    height: 2px;
    background: var(--ink);
  }
  .contacts {
    position: absolute;
    left: 40px;
    top: 330px;
    display: grid;
    grid-template-columns: 300px auto;
    row-gap: 12px;
    column-gap: 20px;
  }
  .contact {
    display: flex;
    align-items: center;
    gap: 16px;
    font-size: 25px;
    color: var(--ink);
  }
  .contact .phone-number { font-style: italic; }
  .icon-box {
    width: 34px;
    height: 30px;
    border-radius: 6px;
    background: var(--blue);
    display: flex;
    align-items: center;
    justify-content: center;
    flex: none;
  }
  .band {
    position: absolute;
    left: 0;
    right: 0;
    bottom: 0;
    height: 95px;
    background: linear-gradient(90deg, var(--blue) 0%, var(--blue-deep) 100%);
  }
  .address {
    position: absolute;
    left: 36px;
    top: 18px;
    display: flex;
    align-items: center;
    gap: 18px;
    color: var(--white);
    font-size: 30px;
    font-style: italic;
  }
  .pin-box {
    width: 36px;
    height: 36px;
    background: var(--white);
    border-radius: 7px;
    display: flex;
    align-items: center;
    justify-content: center;
  }
</style>
</head>
<body>

  <section class="card card-back">
    <div class="brand-name">Corvane<br>Electronics, Inc.</div>
    <div class="back-web">www.corvaneelectronics.com</div>
  </section>

  <section class="card card-front">
    <div class="brand-tab">
      <div class="brand-name">Corvane<br>Electronics, Inc.</div>
    </div>

    <div class="person"><span class="first">Paul</span> Bredesen VP</div>
    <div class="rule"></div>

    <div class="contacts">
      <div class="contact">
        <span class="icon-box">
          <svg width="22" height="18" viewBox="0 0 22 18" fill="none" stroke="#fff" stroke-width="2">
            <path d="M2 6c3-4 15-4 18 0l-3 2-2-2H7L5 8z" fill="#fff"/>
            <rect x="5" y="9" width="12" height="7" rx="2"/>
            <circle cx="11" cy="12.5" r="1.5" fill="#fff"/>
          </svg>
        </span>
        <span class="phone-number">214-555-0187</span>
      </div>
      <div class="contact">
        <span class="icon-box">
          <svg width="22" height="18" viewBox="0 0 22 18" fill="none" stroke="#fff" stroke-width="2">
            <rect x="2" y="4" width="18" height="10"/>
            <polyline points="2,4 11,10 20,4"/>
          </svg>
        </span>
        <span>info@corvaneelectronics.com</span>
      </div>
      <div class="contact">
        <span class="icon-box">
          <svg width="22" height="20" viewBox="0 0 22 20" fill="none" stroke="#fff" stroke-width="2">
            <rect x="6" y="2" width="10" height="5"/>
            <rect x="2" y="7" width="18" height="8" rx="2"/>
            <rect x="6" y="12" width="10" height="6" fill="#1f7cc9"/>
          </svg>
        </span>
        <span class="phone-number">214-555-0143</span>
      </div>
      <div class="contact">
        <span class="icon-box">
          <svg width="22" height="22" viewBox="0 0 22 22" fill="none" stroke="#fff" stroke-width="1.8">
            <circle cx="11" cy="11" r="8.5"/>
            <ellipse cx="11" cy="11" rx="3.8" ry="8.5"/>
            <line x1="2.5" y1="11" x2="19.5" y2="11"/>
          </svg>
        </span>
        <span>www.corvaneelectronics.com</span>
      </div>
    </div>

    <div class="band">
      <div class="address">
        <span class="pin-box">
          <svg width="20" height="26" viewBox="0 0 20 26">
            <path d="M10 1C5 1 1.5 4.8 1.5 9.5 1.5 16 10 25 10 25s8.5-9 8.5-15.5C18.5 4.8 15 1 10 1z" fill="#1f7cc9"/>
            <circle cx="10" cy="9.5" r="3.2" fill="#fff"/>
          </svg>
        </span>
        <span>4518 Maple Crest Blvd. Dallas, TX 75207</span>
      </div>
    </div>
  </section>

</body>
</html>
```